Branded PowerPoint Template Design

Would like a general PowerPoint template customized with my company branding to use in presentations for customers. The company is a talent management consulting and recruiting company called Brenwick & Associates. I would like a design that incorporates the logo colors with a clean and simple look.
Target Market(s)
Slides are typically viewed by HR and Corporate executives either briefing our capabilities or delivering solution results.
Industry/Entity Type
It Company
Requirements
Must have
- Simple clean design that will not draw attention away from the actual presentation. Design should go well with the logo branding and colors.
Should not have
- Should not have any pictures of people

```html
<!DOCTYPE html>
<html lang="en">
<head>
<meta charset="utf-8">
<title>Brenwick &amp; Associates – Presentation Template</title>
<link href="https://fonts.googleapis.com/css2?family=Bebas+Neue&family=Arimo:wght@400;700&display=swap" rel="stylesheet">
<style>
  :root {
    --navy: #241f5c;
    --slide-bg: #f5f6f6;
    --rule-gray: #7b7b7d;
    --stage-light: #6a6a6a;
    --stage-mid: #4b4b4b;
    --stage-dark: #000000;
    --body-ink: #111111;
    --white: #ffffff;
  }
  * { margin: 0; padding: 0; box-sizing: border-box; }
  html, body { width: 999px; height: 1200px; overflow: hidden; }
  body {
    position: relative;
    background: linear-gradient(100deg, var(--stage-light) 0%, var(--stage-mid) 55%, #2a2a2a 85%, var(--stage-dark) 100%);
    font-family: "Arimo", Arial, sans-serif;
  }
  .slide {
    position: absolute;
    left: 137px;
    width: 736px;
    height: 552px;
    background: var(--slide-bg);
    overflow: hidden;
  }
  .slide--title { top: 50px; }
  .slide--content { top: 645px; }

  /* Title slide */
  .brand {
    position: absolute;
    top: 24px; left: 0; width: 100%;
    text-align: center;
  }
  .brand__dot {
    display: block;
    width: 38px; height: 38px;
    margin: 0 auto 8px;
    border-radius: 50%;
    background: var(--navy);
  }
  .brand__name {
    font-family: "Bebas Neue", Impact, sans-serif;
    font-weight: 400;
    font-size: 50px;
    line-height: 1;
    letter-spacing: 1px;
    color: var(--navy);
  }
  .rule { position: absolute; left: 0; width: 100%; height: 7px; background: var(--rule-gray); }
  .rule--top { top: 161px; }
  .rule--bottom { top: 447px; height: 6px; }
  .hero {
    position: absolute; top: 168px; left: 0; width: 100%; height: 279px;
  }
  .hero__photo {
    position: absolute; inset: 0;
    background: linear-gradient(90deg, #d9d6d3 0%, #c9ccd2 30%, #e4e8ec 55%, #eef1f3 80%);
  }
  .hero__panel { position: absolute; top: 0; left: 0; }
  .hero__title {
    position: absolute;
    top: 58px; left: 520px; width: 190px;
    text-align: center;
    font-family: "Bebas Neue", Impact, sans-serif;
    font-weight: 400;
    font-size: 74px;
    line-height: 82px;
    color: var(--white);
  }
  .footer-band {
    position: absolute; left: 0; bottom: 0; width: 100%; height: 19px;
    background: var(--navy);
  }
  .url-pill {
    position: absolute;
    background: var(--navy);
    border: 2px solid var(--white);
    color: var(--white);
    font-weight: 700;
    text-align: center;
  }
  .slide--title .url-pill {
    left: 186px; top: 509px; width: 363px; height: 35px;
    border-radius: 10px;
    font-size: 20px; line-height: 31px;
    letter-spacing: 3px;
  }

  /* Content slide */
  .content__heading {
    position: absolute; top: 34px; left: 39px;
    font-family: "Bebas Neue", Impact, sans-serif;
    font-weight: 400;
    font-size: 57px; line-height: 1;
    color: var(--navy);
  }
  .content__tab { position: absolute; top: 25px; left: 525px; }
  .content__text {
    position: absolute; left: 39px; width: 458px;
    font-size: 15.6px; line-height: 19.6px;
    color: var(--body-ink);
    text-align: justify;
  }
  .content__text--first { top: 106px; }
  .content__text--second { top: 320px; }
  .content__photo { position: absolute; }
  .content__photo--first {
    left: 506px; top: 111px; width: 210px; height: 154px;
    background: linear-gradient(120deg, #dfe3e8 0%, #b9bcc4 45%, #3a3d4c 80%, #cfd2d6 100%);
  }
  .content__photo--second {
    left: 508px; top: 323px; width: 218px; height: 150px;
    background: linear-gradient(110deg, #eceef0 0%, #d5d8dc 40%, #50546a 70%, #a9b4c6 100%);
  }
  .slide--content .footer-band { height: 17px; }
  .slide--content .url-pill {
    left: 482px; top: 519px; width: 211px; height: 21px;
    border-radius: 7px;
    font-size: 14px; line-height: 17px; font-weight: 400;
    letter-spacing: 1.6px;
  }
</style>
</head>
<body>

<section class="slide slide--title">
  <div class="brand">
    <span class="brand__dot"></span>
    <div class="brand__name">Brenwick &amp; Associates</div>
  </div>

  <div class="rule rule--top"></div>
  <div class="hero">
    <div class="hero__photo" role="img" aria-label="Photo of a business team in a bright meeting room reviewing a model"></div>
    <svg class="hero__panel" width="736" height="279" viewBox="0 0 736 279" aria-hidden="true">
      <polygon points="547,0 736,0 736,279 480,279" fill="#241f5c"/>
    </svg>
    <h1 class="hero__title">Title<br>Here</h1>
  </div>
  <div class="rule rule--bottom"></div>

  <div class="footer-band"></div>
  <div class="url-pill">www.abcdefghij.com</div>
</section>

<section class="slide slide--content">
  <h2 class="content__heading">Lorem Ipsum</h2>
  <svg class="content__tab" width="211" height="67" viewBox="0 0 211 67" aria-hidden="true">
    <polygon points="26,0 211,0 211,67 0,67" fill="#241f5c"/>
  </svg>

  <p class="content__text content__text--first">Lorem Ipsum is simply dummy text of the printing and typesetting industry. Lorem Ipsum has been the industry's standard dummy text ever since the 1500s, when an unknown printer took a galley of type and scrambled it to make a type specimen book. It has survived not only five centuries, but also the leap into electronic typesetting, remaining essentially unchanged. It was popularised in the 1960s with the release of Lettrafix sheets containing Lorem Ipsum passages, and more recently with desktop publishing software like Pressline Composer including versions of Lorem Ipsum.</p>
  <div class="content__photo content__photo--first" role="img" aria-label="Photo of colleagues discussing work around a laptop"></div>

  <p class="content__text content__text--second">Lorem Ipsum is simply dummy text of the printing and typesetting industry. Lorem Ipsum has been the industry's standard dummy text ever since the 1500s, when an unknown printer took a galley of type and scrambled it to make a type specimen book. It has survived not only five centuries, but also the leap into electronic typesetting, remaining essentially unchanged. It was popularised in the 1960s with the release of Lettrafix sheets containing Lorem Ipsum passages, and more recently with desktop publishing software like Pressline Composer including versions of Lorem Ipsum.</p>
  <div class="content__photo content__photo--second" role="img" aria-label="Photo of a presenter at a whiteboard addressing a team"></div>

  <div class="footer-band"></div>
  <div class="url-pill">www.abcdefghij.com</div>
</section>

</body>
</html>
```